Business card for Autism Consultancy

I need a double-sided business card for Brightpath Learning Consultancy
Please try to use the colours and graphics in line with our website www.brightpathlearn.nz
Front side
Logo and the name of the company – Brightpath Learning Consultancy
We use Child-Centred, Modern and Innovative approaches
Teaching autistic children to bond, laugh and play
www.brightpathlearn.nz
info@brightpathlearn.nz
phone +64 09 37 615 48
Back side
Photo
Mirela Dunstan
Founder
Postgraduate Autism (Children) Specialist (with Merit)
Qualified by the Faculty of Learning Support and Access Studies (FLSA), Harwell Vale University
mirela@brightpathlearn.nz
phone +64 937 615 48
mobile: +64 20 6283 9150
Please do not convert the text fields to outlines, i.e. I need to be able to edit any text after.
The final design should be either in Adobe Illustrator or Adobe Photoshop format.
The Specs for the business card are:
Full Bleed Size
94 x 58 mm
1110 x 685 pixels
Document Trim Size
91 x 55 mm
1075 x 650 pixels

```html
<!DOCTYPE html>
<html lang="en">
<head>
<meta charset="utf-8">
<title>Brightpath Learning Consultancy – Business Card</title>
<link href="https://fonts.googleapis.com/css2?family=Open+Sans:wght@400;600;700&display=swap" rel="stylesheet">
<style>
  :root {
    --backdrop: #2a2a2c;
    --card: #ffffff;
    --navy: #1b2a5e;
    --teal: #3dbcb4;
    --ink: #3a3a3a;
    --photo-light: #c9a58a;
    --photo-dark: #4a3a30;
  }
  * { margin: 0; padding: 0; box-sizing: border-box; }
  html, body {
    width: 1200px; height: 1000px; overflow: hidden;
    background: var(--backdrop);
    font-family: "Open Sans", Arial, sans-serif;
  }
  .sheet {
    width: 1200px; height: 1000px;
    display: flex; flex-direction: column; align-items: center; justify-content: center; gap: 44px;
  }
  .card {
    position: relative;
    width: 740px; height: 447px;
    background: var(--card);
    box-shadow: 0 10px 30px rgba(0,0,0,.45);
  }

  /* Front */
  .card-front { display: flex; flex-direction: column; align-items: center; padding-top: 52px; }
  .brand { display: flex; align-items: center; gap: 16px; }
  .brand-dot { width: 46px; height: 46px; border-radius: 50%; background: var(--navy); }
  .brand-name { font-size: 30px; font-weight: 700; color: var(--navy); letter-spacing: .3px; }
  .tagline { margin-top: 46px; font-size: 19px; color: var(--navy); }
  .tagline-sub { margin-top: 4px; font-size: 17px; color: var(--teal); }
  .icon-row { margin-top: 28px; display: flex; align-items: center; gap: 8px; }
  .icon-row .rule { width: 56px; height: 1.5px; background: var(--teal); margin: 0 10px; }
  .icon-badge {
    width: 30px; height: 30px; border-radius: 50%; background: var(--navy);
    display: flex; align-items: center; justify-content: center;
  }
  .contact-block { margin-top: 18px; text-align: center; font-size: 19px; line-height: 1.45; color: var(--ink); }

  /* Back */
  .card-back { display: flex; flex-direction: column; align-items: center; padding-top: 30px; }
  .portrait {
    width: 168px; height: 168px; border-radius: 50%;
    border: 4px solid var(--navy);
    background: radial-gradient(circle at 50% 40%, var(--photo-light) 0%, #a57f66 45%, var(--photo-dark) 100%);
  }
  .qualification { margin-top: 22px; font-size: 14px; color: var(--navy); }
  .specialism { margin-top: 6px; font-size: 18px; color: var(--teal); }
  .identity { margin-top: 34px; display: flex; align-items: center; }
  .person { text-align: right; padding-right: 26px; }
  .person-name { font-size: 34px; font-weight: 700; color: var(--navy); line-height: 1.15; }
  .person-role { font-size: 30px; color: var(--teal); line-height: 1.2; }
  .divider { width: 2px; height: 116px; background: var(--navy); }
  .person-contacts { padding-left: 22px; list-style: none; font-size: 21px; color: var(--ink); line-height: 1.5; }
  .person-contacts li { display: flex; align-items: center; gap: 12px; }
  .person-contacts svg { flex: none; }
</style>
</head>
<body>
<main class="sheet">

  <section class="card card-front" aria-label="Card front">
    <div class="brand">
      <span class="brand-dot"></span>
      <span class="brand-name">Brightpath Learning Consultancy</span>
    </div>
    <p class="tagline">We use Child-Centred, Modern and Innovative approaches</p>
    <p class="tagline-sub">Teaching autistic children to bond, laugh and play</p>
    <div class="icon-row">
      <span class="rule"></span>
      <span class="icon-badge">
        <svg width="16" height="16" viewBox="0 0 24 24"><path fill="#fff" d="M6.6 10.8a15 15 0 0 0 6.6 6.6l2.2-2.2c.3-.3.7-.4 1-.2 1.1.4 2.3.6 3.6.6.6 0 1 .4 1 1V20c0 .6-.4 1-1 1A17 17 0 0 1 3 4c0-.6.4-1 1-1h3.5c.6 0 1 .4 1 1 0 1.3.2 2.5.6 3.6.1.3 0 .7-.2 1z"/></svg>
      </span>
      <span class="icon-badge">
        <svg width="16" height="16" viewBox="0 0 24 24"><rect x="3" y="6" width="18" height="12" fill="none" stroke="#fff" stroke-width="2"/><path d="M3 6l9 7 9-7" fill="none" stroke="#fff" stroke-width="2"/></svg>
      </span>
      <span class="icon-badge">
        <svg width="16" height="16" viewBox="0 0 24 24"><circle cx="12" cy="12" r="9" fill="none" stroke="#fff" stroke-width="2"/><ellipse cx="12" cy="12" rx="4" ry="9" fill="none" stroke="#fff" stroke-width="1.6"/><path d="M3 12h18" stroke="#fff" stroke-width="1.6"/></svg>
      </span>
      <span class="rule"></span>
    </div>
    <address class="contact-block" style="font-style:normal">
      +64 09 37 615 48<br>
      info@brightpathlearn.nz<br>
      www.brightpathlearn.nz
    </address>
  </section>

  <section class="card card-back" aria-label="Card back">
    <div class="portrait" role="img" aria-label="Portrait photo of Mirela Dunstan"></div>
    <p class="qualification">Qualified by the Faculty of Learning Support and Access Studies (FLSA), Harwell Vale University</p>
    <p class="specialism">Postgraduate Autism (Children) Specialist (with Merit)</p>
    <div class="identity">
      <div class="person">
        <p class="person-name">Mirela Dunstan</p>
        <p class="person-role">Founder</p>
      </div>
      <span class="divider"></span>
      <ul class="person-contacts">
        <li>
          <svg width="18" height="18" viewBox="0 0 24 24"><path fill="#1b2a5e" d="M6.6 10.8a15 15 0 0 0 6.6 6.6l2.2-2.2c.3-.3.7-.4 1-.2 1.1.4 2.3.6 3.6.6.6 0 1 .4 1 1V20c0 .6-.4 1-1 1A17 17 0 0 1 3 4c0-.6.4-1 1-1h3.5c.6 0 1 .4 1 1 0 1.3.2 2.5.6 3.6.1.3 0 .7-.2 1z"/></svg>
          +64 937 615 48
        </li>
        <li>
          <svg width="18" height="18" viewBox="0 0 24 24"><rect x="6" y="2" width="12" height="20" rx="2" fill="none" stroke="#1b2a5e" stroke-width="2"/><path d="M10 18h4" stroke="#1b2a5e" stroke-width="2"/></svg>
          +64 20 6283 9150
        </li>
        <li>
          <svg width="18" height="18" viewBox="0 0 24 24"><rect x="3" y="6" width="18" height="12" fill="#1b2a5e"/><path d="M3 6l9 7 9-7" fill="none" stroke="#fff" stroke-width="1.6"/></svg>
          mirela@brightpathlearn.nz
        </li>
      </ul>
    </div>
  </section>

</main>
</body>
</html>
```